Modern Informational OBGYN website

Looking for a modern Wordpress website for a general OBGYN practice in Florida with a specialty in High Risk Obstetrics. We had an old Joomla website that crashed and we lost most of the files. It was over 10 years old and needed a refresh anyway.

Our practice serves a multicultural patient population (white, black, Spanish and Indian) and we would like our website to reflect that diversity. Our company colors are sunshine yellow (#ECBF6D) often combined with black, white and steel blue (#7191BE) in the "life" part of our logo (attached) depending on the background. Our tagline is "We're specialist in You!" Overall the site should have a clean modern yet comfortable feel. One that portrays friendliness and competence. At least 6 pages (Home, Obstetrics, Gynecology, News, Patient Education and Resources). Rotating stock pictures or videos are fine for the headers of the pages if the design you're considering calls for it. Interesting and creative use of typography and icons are encouraged.

The home page should have a call to action to schedule an appointment as well as a link to our patient portal. Other than the home and news pages, the other pages should have a similar look and feel. The home page should have sections on "About Us", "Medical Staff" (with pictures and brief bio for 2 male doctors, 2 female midwives and 1 female nurse practitioner), "Services" and "Location". The news page will be a closed blog that will not allow comments or responses. Both the obstetrics and the gynecology pages will have an educational blurb on the respective topics followed by a list of our services for each topic. Would be nice on the obstetrics page to have information and graphics changes that occur during each trimester (but not necessary). The resource page will have sections on at least "Office Forms", Office Policies", "OB Guide" each with multiple downloadable PDF's. Also a section on "Insurance" with a list of all the major insurance plans that we take with links to their company websites. The address, link and map to our hospital and their website can also go on this page. The Patient Education Page can be broken into 3 sections Obstetrics, Gynecology which both will have definition of medical disorders followed by FAQ's and "Helpful Links" which would have links to other website for medical information.

That's all that I can think of right now. The above is to help guide you but I am flexible, if the website design dictates a better flow of information. Looking forward to seeing what you can come up with. Down the road, I will be looking to the winning designer to produce matching brochures, full, half and quarter page media ads to have on hand for the practices further needs.

Target Market(s)

Women looking medical services

Industry/Entity Type

Medical

Coding

Coded - Design and coding required

Number of Pages Required

5+ page

Font styles to use
Sans Serif
Script

Colors

Designer to choose colors to be used in the design.

Requirements
Must have
• None. See projects description for suggestions
Nice to have
• infographics like information on stages of pregnancy on the obstetrics page

```html
<!DOCTYPE html>
<html lang="en">
<head>
<meta charset="utf-8">
<title>Brightway ObGyn – Home</title>
<link href="https://fonts.googleapis.com/css2?family=Roboto:wght@400;500;700;900&family=Roboto+Slab:wght@600;700&display=swap" rel="stylesheet">
<style>
:root{
  --sun:#ECBF6D;
  --sun-deep:#E0A945;
  --steel:#7191BE;
  --steel-dark:#5F7FB0;
  --ink:#1d1d1d;
  --text:#555;
  --muted:#777;
  --cream:#F7EEDD;
  --white:#fff;
  --black:#000;
}
*{box-sizing:border-box;margin:0;padding:0}
html,body{width:1200px;height:4511px;overflow:hidden}
body{position:relative;font-family:'Roboto',sans-serif;color:var(--ink);background:var(--white)}
.abs{position:absolute}
.topbar{left:0;top:0;width:1200px;height:42px;background:var(--sun);font-size:13px;font-weight:500;color:#222}
.topbar .notice{left:112px;top:13px}
.topbar .links{right:112px;top:13px;display:flex;gap:34px}
.nav{left:0;top:42px;width:1200px;height:84px;background:var(--white)}
.brand{left:112px;top:64px;font-family:'Roboto',sans-serif;font-weight:900;font-size:28px;color:var(--sun-deep);display:flex;align-items:center;gap:8px}
.brand .dot{width:14px;height:14px;border-radius:50%;background:var(--sun)}
.menu{top:76px;left:320px;display:flex;gap:20px;font-size:13px;font-weight:500}
.menu .active{color:var(--sun-deep)}
.btn{display:inline-flex;align-items:center;justify-content:center;gap:8px;border-radius:24px;color:#fff;font-size:12px;font-weight:700;text-transform:uppercase;letter-spacing:.2px}
.btn-sun{background:var(--sun)}
.btn-steel{background:var(--steel)}
.hero{left:0;top:126px;width:1200px;height:800px;overflow:hidden}
.hero .photo{position:absolute;inset:0;background:linear-gradient(100deg,#5b5a2e 0%,#7b7a3a 35%,#a59a55 60%,#c9b073 80%,#8a8044 100%)}
.hero h1{left:112px;top:176px;font-size:68px;line-height:70px;font-weight:900;color:#fff;letter-spacing:.5px}
.hero p{left:112px;top:336px;width:600px;font-size:14.5px;line-height:26px;color:#fff;font-weight:500}
.hero .btn{left:112px;top:410px;width:243px;height:42px}
.section-title{font-family:'Roboto Slab',serif;font-size:30px;font-weight:700;color:var(--ink);text-transform:uppercase}
.section-title .hl{color:var(--sun)}
.about-photo{left:116px;top:893px;width:441px;height:441px;border-radius:50%;border:5px solid var(--sun);background:linear-gradient(135deg,#7a3a24,#c46a3a 50%,#3e2418)}
.about-title{left:640px;top:938px}
.about-text{left:640px;top:994px;width:446px;font-size:13.5px;line-height:26.5px;color:var(--text);text-align:justify}
.about .btn{left:640px;top:1253px;width:150px;height:42px}
.services{left:0;top:1290px;width:1200px;height:737px;background:var(--steel);overflow:hidden}
.services .shape-top{position:absolute;left:0;top:0}
.services-title{left:0;width:1200px;text-align:center;top:210px;color:#fff}
.services-title .rest{color:var(--ink)}
.services .ring{position:absolute;left:355px;top:440px;width:490px;height:490px;border-radius:50%;border:14px solid var(--sun)}
.services .model{left:487px;top:278px;width:240px;height:459px;border-radius:120px 120px 0 0;background:linear-gradient(180deg,#5a4030 0%,#8c6a50 35%,#7d7160 60%,#9b8e78 100%)}
.svc-icon{width:64px;height:64px;border-radius:50%;background:var(--steel-dark);border:3px solid #8ea7cb;display:flex;align-items:center;justify-content:center}
.svc{color:#fff;font-size:13px;line-height:19px}
.svc h3{font-size:18px;font-weight:700;margin-bottom:4px}
.svc.left{text-align:right}
.team-title{left:0;width:1200px;text-align:center;top:2098px}
.member{text-align:center;width:330px}
.member .avatar{width:280px;height:280px;border-radius:50%;margin:0 auto 28px;background:radial-gradient(circle at 50% 40%,#bfc3c7,#7d8286)}
.member .avatar.gold{border:5px solid var(--sun)}
.member h4{font-size:20px;font-weight:700}
.member .role{font-size:14px;color:var(--muted);margin-top:6px}
.member .bio{font-size:13px;line-height:22px;color:var(--muted);margin-top:16px}
.location{left:0;top:2996px;width:1200px;height:700px;background:var(--cream)}
.loc-title{left:0;width:1200px;text-align:center;top:3050px}
.card{width:315px;height:331px;background:#FBF4E6;box-shadow:0 2px 10px rgba(0,0,0,.12);top:3124px}
.card .map{position:absolute;left:4px;top:4px;width:307px;height:216px;background:linear-gradient(135deg,#e7e3da,#d9dccf 50%,#e3dfd3)}
.card .tag{position:absolute;left:70px;top:12px;width:175px;height:31px;background:var(--sun);color:#fff;font-size:11px;font-weight:700;display:flex;align-items:center;justify-content:center;text-transform:uppercase}
.card .addr{position:absolute;left:42px;top:238px;width:250px;font-size:12.5px;line-height:20px;font-weight:700}
.card .phones{position:absolute;left:18px;top:292px;font-size:12.5px;font-weight:700;display:flex;gap:26px}
.card .phones span{display:flex;align-items:center;gap:8px}
.card .pin{position:absolute;left:18px;top:242px}
.stage-title{left:0;width:1200px;text-align:center;top:3650px}
.trim{font-size:14px;font-weight:500;text-align:center}
.bracket{border:2px dashed #444;border-bottom:none;height:18px}
.fetus{border-radius:50%;background:radial-gradient(circle at 45% 45%,#f3a59a,#c8475a 60%,#8e1f3a)}
.month{font-size:12px;font-weight:500;text-align:center;width:90px}
.footer{left:0;top:4000px;width:1200px;height:460px;background:var(--black);overflow:hidden}
.f-brand{left:114px;top:4320px;font-weight:900;font-size:34px;color:#fff;display:flex;align-items:center;gap:10px}
.f-brand .dot{width:16px;height:16px;border-radius:50%;background:var(--sun)}
.f-contact{color:#fff;display:flex;align-items:center;gap:16px;top:4272px}
.f-contact .ico{width:46px;height:46px;border-radius:50%;border:1.5px solid #fff;display:flex;align-items:center;justify-content:center}
.f-contact .lbl{font-size:12px;font-weight:700;text-transform:uppercase}
.f-contact .val{font-size:13px;margin-top:4px;line-height:18px}
.f-contact .val.big{font-size:19px;font-weight:700}
.f-line{left:392px;top:4342px;width:698px;height:1px;background:#555}
.f-menu{left:393px;top:4367px;display:flex;gap:22px;color:#fff;font-size:13px;font-weight:500}
.social{top:4357px;width:34px;height:34px;border-radius:50%;border:1.5px solid #fff}
.copyright{left:0;top:4459px;width:1200px;height:52px;background:var(--sun);font-size:13px;text-align:center;line-height:52px;color:#222}
</style>
</head>
<body>

<div class="abs topbar">
  <div class="abs notice">Now accepting Telehealth appointments. Call to schedule a virtual visit.</div>
  <div class="abs links"><span>♥ Bill Pay / Patient Portal</span><span>☎ 888-555-0142</span></div>
</div>

<header class="abs nav">
  <div class="abs brand" style="top:22px;left:112px"><span class="dot"></span>BRIGHTWAY</div>
  <nav class="abs menu" style="top:34px">
    <span class="active">Home</span><span>Obstetrics</span><span>Gynecology</span><span>News</span><span>Patient Education</span><span>Resources</span>
  </nav>
  <a class="abs btn btn-sun" style="left:845px;top:21px;width:242px;height:44px">Schedule an appointment ▦</a>
</header>

<section class="abs hero">
  <div class="photo" role="img" aria-label="Expectant mother standing in a sunlit meadow, holding her belly"></div>
  <h1 class="abs">WE'RE SPECIALIST<br>IN YOU!</h1>
  <p class="abs">At Brightway , the focus is on the whole patient and making sure the treatment programs developed for each patient have the best chance for success.</p>
  <a class="abs btn btn-steel">Schedule an appointment ▦</a>
  <svg class="abs" style="left:0;top:620px" width="1200" height="180" viewBox="0 0 1200 180">
    <path d="M0 164 Q600 -40 1200 164 L1200 180 L0 180Z" fill="var(--sun)"/>
    <path d="M0 180 Q600 -20 1200 180Z" fill="#fff"/>
  </svg>
</section>

<section class="about">
  <div class="abs about-photo" role="img" aria-label="Two expectant mothers smiling together"></div>
  <h2 class="abs section-title about-title"><span class="hl">About</span> us</h2>
  <p class="abs about-text">At Brightway you will be a part of a team made up of providers, medical assistants and health specialists that help coordinate your health care. This is your Circle of Care, at which you are the center. Engaging you in your treatment plan is the core of PCMC. At Brightway, we want you to be involved in a variety of ways: we will ask for your input about medical decisions and treatment. We will work with you to develop self-management goals and care plans, we will ask you for feedback in the way of patient satisfaction surveys and we will provide you with access to resources to support your medical care.</p>
  <a class="abs btn btn-steel">Learn more ›</a>
</section>

<section class="abs services">
  <svg class="shape-top" width="1200" height="160" viewBox="0 0 1200 160">
    <path d="M0 0 L1200 0 L1200 6 Q600 270 0 6Z" fill="var(--sun)"/>
    <path d="M0 0 L1200 0 Q600 250 0 0Z" fill="#fff"/>
  </svg>
  <h2 class="abs section-title services-title"><span class="hl">Our</span> <span class="rest">Services</span></h2>
  <div class="ring"></div>
  <div class="abs model" role="img" aria-label="Smiling pregnant woman in a striped top"></div>

  <div class="abs svc left" style="left:200px;top:428px;width:222px"><h3>Pharmacy</h3>Lorem ipsum dolor sit amet, consectetur adipiscing</div>
  <div class="abs svc left" style="left:110px;top:520px;width:216px"><h3>TeleHealth</h3>Lorem ipsum dolor sit amet, consectetur adipiscing</div>
  <div class="abs svc left" style="left:80px;top:634px;width:214px"><h3>Health</h3>Lorem ipsum dolor sit amet, consectetur adipiscing</div>
  <div class="abs svc" style="left:796px;top:436px;width:200px"><h3>Integrated Services</h3>Lorem ipsum dolor sit amet, consectetur adipiscing</div>
  <div class="abs svc" style="left:873px;top:524px;width:200px"><h3>Education</h3>Lorem ipsum dolor sit amet, consectetur adipiscing</div>
  <div class="abs svc" style="left:899px;top:634px;width:200px"><h3>Social Services</h3>Lorem ipsum dolor sit amet, consectetur adipiscing</div>

  <div class="abs svc-icon" style="left:455px;top:426px"><svg width="28" height="28" viewBox="0 0 24 24" fill="none" stroke="#fff" stroke-width="2"><path d="M12 2v20M8 6h8M6 10c4 0 8 2 6 6M18 10c-4 0-8 2-6 6"/></svg></div>
  <div class="abs svc-icon" style="left:357px;top:523px"><svg width="28" height="28" viewBox="0 0 24 24" fill="none" stroke="#fff" stroke-width="2"><rect x="3" y="4" width="18" height="13" rx="1"/><path d="M8 21h8M12 17v4"/></svg></div>
  <div class="abs svc-icon" style="left:327px;top:640px"><svg width="28" height="28" viewBox="0 0 24 24" fill="none" stroke="#fff" stroke-width="2"><path d="M12 20s-8-5-8-11a4 4 0 0 1 8-1 4 4 0 0 1 8 1c0 6-8 11-8 11z"/><path d="M6 12h3l2-3 2 5 2-2h3"/></svg></div>
  <div class="abs svc-icon" style="left:706px;top:439px"><svg width="28" height="28" viewBox="0 0 24 24" fill="none" stroke="#fff" stroke-width="2"><circle cx="12" cy="12" r="8"/><path d="M12 4v16M4 12h16"/></svg></div>
  <div class="abs svc-icon" style="left:783px;top:526px"><svg width="28" height="28" viewBox="0 0 24 24" fill="none" stroke="#fff" stroke-width="2"><circle cx="7" cy="6" r="2.5"/><path d="M4 21v-8h6M12 4h9v9h-9z"/></svg></div>
  <div class="abs svc-icon" style="left:809px;top:640px"><svg width="28" height="28" viewBox="0 0 24 24" fill="none" stroke="#fff" stroke-width="2"><circle cx="12" cy="7" r="3"/><path d="M3 20c3-1 5-4 9-4s6 3 9 4"/></svg></div>
</section>

<section class="team">
  <h2 class="abs section-title team-title"><span class="hl">Leadership</span> team</h2>
  <div class="abs member" style="left:107px;top:2167px"><div class="avatar" role="img" aria-label="Portrait of the chief executive officer"></div><h4>Daniel Reyes, MD</h4><div class="role">Chief Executive Officer</div></div>
  <div class="abs member" style="left:436px;top:2167px"><div class="avatar" role="img" aria-label="Portrait of the director of pharmacy"></div><h4>Marcus Hale, PharmD</h4><div class="role">Director of Pharmacy</div></div>
  <div class="abs member" style="left:765px;top:2167px"><div class="avatar" role="img" aria-label="Portrait of the director of medical services"></div><h4>Helen Carter</h4><div class="role">Director of Medical Services</div></div>
  <div class="abs member" style="left:270px;top:2530px"><div class="avatar gold" role="img" aria-label="Portrait of the director of human resources"></div><h4>Andrea Lopez</h4><div class="role">Director of Human Resources</div><p class="bio">Lorem ipsum dolor sit amet, consectetur adipiscing elit, sed do eiusmod tempor incididunt ut labore et dolore magna aliqua. Ut enim ad minim</p></div>
  <div class="abs member" style="left:601px;top:2535px"><div class="avatar" role="img" aria-label="Portrait of the nurse in a clinic"></div><h4>Grace Ellison Moore</h4><div class="role">Nurse</div></div>
</section>

<section class="abs location" role="img" aria-label="Soft cream backdrop of a mother with her baby"></section>
<h2 class="abs section-title loc-title"><span class="hl">Our</span> location</h2>

<div class="abs card" style="left:109px">
  <div class="map" role="img" aria-label="Street map of the Cedar Junction office"></div>
  <div class="tag">Cedar Junction</div>
  <svg class="pin" width="14" height="18" viewBox="0 0 24 30"><path d="M12 0a10 10 0 0 0-10 10c0 8 10 20 10 20s10-12 10-20A10 10 0 0 0 12 0z" fill="var(--steel)"/><circle cx="12" cy="10" r="4" fill="#fff"/></svg>
  <div class="addr">1450 W. Meadow Avenue, Suite B-10, Cedar Junction, AZ 85000</div>
  <div class="phones"><span><b style="color:var(--steel)">☎</b>(480) 555-0150</span><span><b style="color:var(--steel)">▤</b>(480) 555-0151</span></div>
</div>
<div class="abs card" style="left:443px">
  <div class="map" role="img" aria-label="Street map of the Center for Women"></div>
  <div class="tag">Center for Women</div>
  <svg class="pin" width="14" height="18" viewBox="0 0 24 30"><path d="M12 0a10 10 0 0 0-10 10c0 8 10 20 10 20s10-12 10-20A10 10 0 0 0 12 0z" fill="var(--steel)"/><circle cx="12" cy="10" r="4" fill="#fff"/></svg>
  <div class="addr">1450 W. Meadow Avenue, Suite B-10, Cedar Junction, AZ 85000</div>
  <div class="phones"><span><b style="color:var(--steel)">☎</b>(480) 555-0156</span><span><b style="color:var(--steel)">▤</b>(480) 555-0151</span></div>
</div>
<div class="abs card" style="left:776px">
  <div class="map" role="img" aria-label="Street map of the Marlow office"></div>
  <div class="tag">Marlow</div>
  <svg class="pin" width="14" height="18" viewBox="0 0 24 30"><path d="M12 0a10 10 0 0 0-10 10c0 8 10 20 10 20s10-12 10-20A10 10 0 0 0 12 0z" fill="var(--steel)"/><circle cx="12" cy="10" r="4" fill="#fff"/></svg>
  <div class="addr">720 N. Orchard Road, Marlow, AZ 85002</div>
  <div class="phones"><span><b style="color:var(--steel)">☎</b>(520) 555-0146</span><span><b style="color:var(--steel)">▤</b>(520) 555-0105</span></div>
</div>

<svg class="abs" style="left:0;top:3500px" width="1200" height="200" viewBox="0 0 1200 200">
  <path d="M0 140 Q600 -30 1200 140 L1200 200 L0 200Z" fill="var(--sun)"/>
  <path d="M0 148 Q600 -20 1200 148 L1200 200 L0 200Z" fill="#fff"/>
</svg>
<section class="abs" style="left:0;top:3690px;width:1200px;height:330px;background:#fff"></section>

<h2 class="abs section-title stage-title"><span class="hl">Stages of</span> pregnancy</h2>
<div class="abs trim" style="left:125px;top:3748px;width:235px">I TRIMESTER<div class="bracket" style="margin-top:8px"></div></div>
<div class="abs trim" style="left:435px;top:3748px;width:235px">II TRIMESTER<div class="bracket" style="margin-top:8px"></div></div>
<div class="abs trim" style="left:780px;top:3748px;width:235px">III TRIMESTER<div class="bracket" style="margin-top:8px"></div></div>

<div class="abs fetus" style="left:117px;top:3842px;width:58px;height:70px" role="img" aria-label="Fetus at one month"></div>
<div class="abs fetus" style="left:203px;top:3838px;width:64px;height:74px" role="img" aria-label="Fetus at two months"></div>
<div class="abs fetus" style="left:295px;top:3822px;width:76px;height:92px" role="img" aria-label="Fetus at three months"></div>
<div class="abs fetus" style="left:403px;top:3818px;width:84px;height:100px" role="img" aria-label="Fetus at four months"></div>
<div class="abs fetus" style="left:517px;top:3818px;width:88px;height:104px" role="img" aria-label="Fetus at five months"></div>
<div class="abs fetus" style="left:629px;top:3814px;width:92px;height:108px" role="img" aria-label="Fetus at six months"></div>
<div class="abs fetus" style="left:742px;top:3812px;width:92px;height:110px" role="img" aria-label="Fetus at seven months"></div>
<div class="abs fetus" style="left:857px;top:3810px;width:94px;height:112px" role="img" aria-label="Fetus at eight months"></div>
<div class="abs fetus" style="left:971px;top:3806px;width:98px;height:116px" role="img" aria-label="Fetus at nine months"></div>

<div class="abs month" style="left:100px;top:3953px">1 MONTH</div>
<div class="abs month" style="left:190px;top:3953px">2 MONTH</div>
<div class="abs month" style="left:288px;top:3953px">3 MONTH</div>
<div class="abs month" style="left:400px;top:3953px">4 MONTH</div>
<div class="abs month" style="left:516px;top:3953px">5 MONTH</div>
<div class="abs month" style="left:630px;top:3953px">6 MONTH</div>
<div class="abs month" style="left:743px;top:3953px">7 MONTH</div>
<div class="abs month" style="left:859px;top:3953px">8 MONTH</div>
<div class="abs month" style="left:975px;top:3953px">9 MONTH</div>

<footer class="abs footer">
  <svg class="abs" style="left:0;top:0" width="1200" height="200" viewBox="0 0 1200 200">
    <path d="M0 0 L1200 0 L1200 18 Q600 310 0 18Z" fill="var(--sun)"/>
    <path d="M0 0 L1200 0 L1200 8 Q600 290 0 8Z" fill="#fff"/>
  </svg>
</footer>
<div class="abs f-brand"><span class="dot"></span>BRIGHTWAY</div>
<div class="abs f-contact" style="left:392px">
  <div class="ico"><svg width="18" height="14" viewBox="0 0 24 18"><rect width="24" height="18" rx="2" fill="#fff"/><path d="M1 2l11 8 11-8" stroke="#000" stroke-width="2" fill="none"/></svg></div>
  <div><div class="lbl">Email us</div><div class="val">contact@brightwayhc.org</div></div>
</div>
<div class="abs f-contact" style="left:618px">
  <div class="ico"><svg width="18" height="18" viewBox="0 0 24 24"><path d="M6 2l4 4-2 3c1 3 4 6 7 7l3-2 4 4-3 4C10 22 2 14 2 5z" fill="#fff"/></svg></div>
  <div><div class="lbl">Call us</div><div class="val big">888-555-0142</div></div>
</div>
<div class="abs f-contact" style="left:852px;top:4264px">
  <div class="ico"><svg width="14" height="18" viewBox="0 0 24 30"><path d="M12 0a10 10 0 0 0-10 10c0 8 10 20 10 20s10-12 10-20A10 10 0 0 0 12 0z" fill="#fff"/><circle cx="12" cy="10" r="4" fill="#000"/></svg></div>
  <div><div class="lbl">Address</div><div class="val">PO Box 4410 Marlow,<br>AZ 85001</div></div>
</div>
<div class="abs f-line"></div>
<nav class="abs f-menu"><span>Home</span><span>Obstetrics</span><span>Gynecology</span><span>News</span><span>Patient Education</span><span>Resources</span></nav>
<div class="abs social" style="left:964px"></div>
<div class="abs social" style="left:1010px"></div>
<div class="abs social" style="left:1055px"></div>

<div class="abs copyright">© 2022 Brightway ObGyn. All Rights Reserved</div>

</body>
</html>
```